New business card for civil engineering company - "Keystone Audit"

We need a business card designed for our new structural engineering company.

The company name is "Keystone Audit" logo files attached.

We would like the following:
* Two-sided card
* Simple design

Information to be placed on the card:
Name - Marcus Dellow
Job Title - Director / Structural Engineer
Credentials - BEng(Hons), CPEng, CMengNZ, IntPE(NZ)
Email - marcus.dellow@keystoneaudit.co.nz
mobile - 0219364058
website - www.keystoneaudit.co.nz

```html
<!DOCTYPE html>
<html lang="en">
<head>
<meta charset="utf-8">
<title>Keystone Audit – Business Card</title>
<link href="https://fonts.googleapis.com/css2?family=Barlow:wght@400;500;700&display=swap" rel="stylesheet">
<style>
  :root {
    --bg: #ffffff;
    --ink: #3f3f41;
    --ink-soft: #4a4a4c;
    --brand: #58585a;
    --brand-tint: #a9aaad;
  }
  html, body {
    margin: 0;
    padding: 0;
    width: 1200px;
    height: 1000px;
    overflow: hidden;
    background: var(--bg);
  }
  .card {
    position: relative;
    width: 1200px;
    height: 1000px;
    font-family: "Barlow", Arial, sans-serif;
    color: var(--ink);
  }
  .identity {
    position: absolute;
    left: 127px;
    top: 262px;
  }
  .identity__name {
    margin: 0;
    font-size: 76px;
    line-height: 1;
    letter-spacing: 3px;
    text-transform: uppercase;
    color: var(--ink);
    font-weight: 400;
  }
  .identity__first { font-weight: 700; }
  .identity__role {
    margin: 12px 0 0;
    font-size: 36px;
    font-weight: 400;
    letter-spacing: 0.5px;
    color: var(--ink-soft);
  }
  .identity__credentials {
    margin: 8px 0 0;
    font-size: 30px;
    font-weight: 400;
    letter-spacing: 0.5px;
    color: var(--ink-soft);
  }
  .contacts {
    position: absolute;
    left: 127px;
    top: 568px;
    margin: 0;
    padding: 0;
    list-style: none;
  }
  .contacts__item {
    display: flex;
    align-items: center;
    height: 48px;
    margin-bottom: 16px;
    font-size: 32px;
    letter-spacing: 0.5px;
    color: var(--ink-soft);
  }
  .contacts__icon {
    width: 32px;
    height: 48px;
    margin-right: 27px;
    flex: none;
  }
  .brand {
    position: absolute;
    right: 131px;
    top: 470px;
    text-align: right;
  }
  .brand__square {
    display: block;
    width: 130px;
    height: 130px;
    margin-left: auto;
    background: var(--brand-tint);
  }
  .brand__name {
    display: block;
    margin-top: 22px;
    font-size: 40px;
    font-weight: 500;
    letter-spacing: 1px;
    color: var(--brand);
  }
</style>
</head>
<body>
<main class="card">
  <section class="identity">
    <h1 class="identity__name"><span class="identity__first">Marcus</span> Dellow</h1>
    <p class="identity__role">Director / Structural Engineer</p>
    <p class="identity__credentials">BEng(Hons), CPEng, CMengNZ, IntPE(NZ)</p>
  </section>

  <ul class="contacts">
    <li class="contacts__item">
      <svg class="contacts__icon" viewBox="0 0 32 48" aria-hidden="true">
        <rect x="0" y="13" width="31" height="21" rx="2" fill="#2a2a2a"/>
        <polyline points="1,15 15.5,26 30,15" fill="none" stroke="#ffffff" stroke-width="2"/>
      </svg>
      <span>marcus.dellow@keystoneaudit.co.nz</span>
    </li>
    <li class="contacts__item">
      <svg class="contacts__icon" viewBox="0 0 32 48" aria-hidden="true">
        <g transform="rotate(-22 16 24)">
          <rect x="6" y="4" width="20" height="40" rx="3" fill="none" stroke="#2a2a2a" stroke-width="3"/>
          <rect x="9" y="8" width="14" height="10" fill="#2a2a2a"/>
          <g fill="#2a2a2a">
            <rect x="9" y="22" width="3.5" height="3.5"/><rect x="14.3" y="22" width="3.5" height="3.5"/><rect x="19.5" y="22" width="3.5" height="3.5"/>
            <rect x="9" y="27.5" width="3.5" height="3.5"/><rect x="14.3" y="27.5" width="3.5" height="3.5"/><rect x="19.5" y="27.5" width="3.5" height="3.5"/>
            <rect x="9" y="33" width="3.5" height="3.5"/><rect x="14.3" y="33" width="3.5" height="3.5"/><rect x="19.5" y="33" width="3.5" height="3.5"/>
          </g>
        </g>
      </svg>
      <span>0219364058</span>
    </li>
    <li class="contacts__item">
      <svg class="contacts__icon" viewBox="0 0 32 48" aria-hidden="true">
        <g fill="none" stroke="#2a2a2a" stroke-width="2">
          <circle cx="16" cy="21" r="14.5"/>
          <ellipse cx="16" cy="21" rx="6.5" ry="14.5"/>
          <line x1="16" y1="6.5" x2="16" y2="35.5"/>
          <line x1="1.5" y1="21" x2="30.5" y2="21"/>
          <line x1="4" y1="13" x2="28" y2="13"/>
          <line x1="4" y1="29" x2="28" y2="29"/>
        </g>
      </svg>
      <span>www.keystoneaudit.co.nz</span>
    </li>
  </ul>

  <div class="brand">
    <span class="brand__square" aria-hidden="true"></span>
    <span class="brand__name">Keystone Audit</span>
  </div>
</main>
</body>
</html>
```